Business card to be used as a flyer

This business card should do the trick of a full scale flyer , so basicaly from the business card itself we only keep the size and remove the clasical name , position , company name (etc).
This business cards should be , like said above, used as promo tool, being gived to different girls . So base one : the design is girls oriented.
Colors : black background . We will use gold (color) folio for the text.
Attached you have our logo, but this should not be a proiminent part of the design . You can use only the cat head instead.
Target Market(s)
Girls / Women
Contact Information for Business Card
> black background , gold / folio text and elements
> cat head from the logo in a creative way do be displayed
> proieminent text "your path to success starts here"
> contact details phone and website .
www.velvadrome.ro (website) and 0741263519 (phone)
Font styles to use
Colors
Designer to choose only greyscale colors for use in the design.
Look and feel

```html
<!DOCTYPE html>
<html lang="en">
<head>
<meta charset="utf-8">
<title>Velvadrome Studio – Business Card</title>
<link rel="stylesheet" href="https://fonts.googleapis.com/css2?family=Arvo:wght@400;700&display=swap">
<style>
  :root {
    --backdrop: #1c1c1c;
    --card-black: #0f0f0f;
    --gold-deep: #c2a444;
    --gold-mid: #dcc26a;
    --gold-light: #f8eba3;
    --ink: #111111;
  }
  html, body {
    margin: 0;
    width: 1200px;
    height: 1015px;
    overflow: hidden;
    background: radial-gradient(ellipse at center, #2e2e2e 0%, var(--backdrop) 70%, #0d0d0d 100%);
    font-family: "Arvo", serif;
  }
  .canvas {
    position: relative;
    width: 1200px;
    height: 1015px;
  }
  .card {
    position: absolute;
    left: 250px;
    width: 700px;
    height: 400px;
    overflow: hidden;
    background: var(--card-black);
    box-shadow: 0 14px 30px rgba(0,0,0,0.6);
  }
  .card--contact { top: 70px; }
  .card--slogan { top: 545px; }
  .card__art {
    position: absolute;
    inset: 0;
    width: 100%;
    height: 100%;
  }
  .card--slogan .card__art { transform: rotate(180deg); }

  .contact {
    position: absolute;
    left: 55px;
    top: 55px;
    margin: 0;
    color: var(--ink);
    font-size: 26px;
    line-height: 1.6;
    letter-spacing: 0.5px;
  }
  .contact__phone { display: block; padding-left: 40px; }
  .contact__web { display: block; }

  .brand {
    position: absolute;
    color: var(--gold-mid);
    font-weight: 700;
    font-size: 28px;
    letter-spacing: 2px;
    text-transform: uppercase;
    display: flex;
    align-items: center;
    gap: 12px;
    white-space: nowrap;
  }
  .brand__dot {
    width: 13px;
    height: 13px;
    border-radius: 50%;
    background: var(--gold-mid);
  }
  .card--contact .brand { right: 30px; top: 290px; }
  .card--slogan .brand { left: 40px; top: 80px; }

  .slogan {
    position: absolute;
    right: 45px;
    bottom: 60px;
    margin: 0;
    color: var(--ink);
    font-weight: 700;
    font-size: 36px;
    line-height: 1.2;
    text-align: center;
  }
  .slogan span { display: block; }
</style>
</head>
<body>
<main class="canvas">

  <section class="card card--contact" aria-label="Card front with contact details">
    <svg class="card__art" viewBox="0 0 700 400" preserveAspectRatio="none" aria-hidden="true">
      <defs>
        <linearGradient id="goldSheen" x1="0" y1="1" x2="1" y2="0">
          <stop offset="0" stop-color="#c9ab4c"/>
          <stop offset="0.45" stop-color="#f8eba3"/>
          <stop offset="1" stop-color="#c2a444"/>
        </linearGradient>
      </defs>
      <rect width="700" height="400" fill="url(#goldSheen)"/>
      <path d="M0,400 L0,345 C250,335 300,190 430,110 C520,55 620,30 700,35 L700,400 Z" fill="#0f0f0f"/>
      <path d="M0,400 L0,355 C255,345 310,200 440,122 C530,68 625,46 700,50 L700,400 Z" fill="url(#goldSheen)"/>
      <path d="M0,400 L0,362 C262,352 320,210 450,132 C540,80 630,58 700,62 L700,400 Z" fill="#0f0f0f"/>
    </svg>
    <p class="contact">
      <span class="contact__phone">0741263519</span>
      <span class="contact__web">www.velvadrome.ro</span>
    </p>
    <div class="brand"><span class="brand__dot"></span>Velvadrome studio</div>
  </section>

  <section class="card card--slogan" aria-label="Card back with slogan">
    <svg class="card__art" viewBox="0 0 700 400" preserveAspectRatio="none" aria-hidden="true">
      <defs>
        <linearGradient id="goldSheenBack" x1="0" y1="1" x2="1" y2="0">
          <stop offset="0" stop-color="#c9ab4c"/>
          <stop offset="0.5" stop-color="#f8eba3"/>
          <stop offset="1" stop-color="#c2a444"/>
        </linearGradient>
      </defs>
      <rect width="700" height="400" fill="url(#goldSheenBack)"/>
      <path d="M0,400 L0,345 C250,335 300,190 430,110 C520,55 620,30 700,35 L700,400 Z" fill="#0f0f0f"/>
      <path d="M0,400 L0,355 C255,345 310,200 440,122 C530,68 625,46 700,50 L700,400 Z" fill="url(#goldSheenBack)"/>
      <path d="M0,400 L0,362 C262,352 320,210 450,132 C540,80 630,58 700,62 L700,400 Z" fill="#0f0f0f"/>
    </svg>
    <div class="brand"><span class="brand__dot"></span>Velvadrome studio</div>
    <h1 class="slogan">
      <span>Your Path To</span>
      <span>Success</span>
      <span>Starts Here</span>
    </h1>
  </section>

</main>
</body>
</html>
```